Referral Card thats different from the rest

Business card size-

Referral card that will be given to clients, in turn they will pass it on to their friends.

The referee will add their name and address, and friends name to card before it is passed on

Referee gets 2 FREE movie tickets

Friend gets $25 OFF their service

Company is an electrical contracting company specialising in the domestic market.

I would like the card to be fun not so serious!
Completely open minded to any and every creative idea!

attached is 2 photo of an example of what another business has, i am trying to achieve something similiar
Updates

I have increased the budget, ;)

i have added 2 x photos of what i am trying to achieve. this is from another business, I am after something similar to this
Thanks

I have updated the design brief.
this should help make it easir and more clear
Thanks

Target Market(s)

Home owners from 30yrs +

Industry/Entity Type

Electrical

Requirements
Must have
• Logo - Not a main feature of card
1300 846 572 on both sides
Lic no: 418695D (doesn’t have to be big) prefer on back

The main feature of the front of the card is the 2 free movie tickets for Referee & $25 OFF Friends first bill

HOW ABOUT TWO FREE MOVIE TICKETS?
It is easy! Know someone who needs an electrician? Maybe a friend, family member, relative or work colleague.
Tell them about us, and we will take $25 off their first bill and give you two FREE Movie Tickets just for introducing us.
To make a referral fill out this card and give it to your friend.

Recommended By:____________
Address:__________________
Frinds name: _____________

*this offer is only valued for work over $55. Non transferable for cash. This coupon is limited to 1 per customer, not to be used in conjunction with any other offer
Nice to have
• Catchy heading on card
example- tell a friend for cash card, (if i was giving away cash vouchers..)

example- keep me in your wallet and pass me on

```html
<!DOCTYPE html>
<html lang="en">
<head>
<meta charset="utf-8">
<title>Referral Card – Bright Spark Electrical</title>
<link rel="stylesheet" href="https://fonts.googleapis.com/css2?family=Open+Sans:wght@400;600&family=Bitter:ital,wght@0,700;1,700&family=Arimo:wght@400;700&display=swap">
<style>
  :root{
    --page:#f4f4f2;
    --frame:#fff200;
    --sky:#3ea7ee;
    --sun:#ffec3a;
    --orange:#f07a12;
    --orange-light:#f6a12c;
    --ink:#1a1a1a;
    --white:#ffffff;
    --accent-blue:#2f8fe0;
    --brand-orange:#e8721b;
    --slogan:#c85a16;
  }
  *{box-sizing:border-box;margin:0;padding:0}
  html,body{width:1200px;height:1048px;overflow:hidden;background:var(--page)}
  .canvas{position:relative;width:1200px;height:1048px}

  .card{position:absolute;background:var(--frame);padding:15px}
  .card--front{left:262px;top:45px;width:720px;height:462px}
  .card--back{left:258px;top:548px;width:724px;height:460px}
  .card__face{position:relative;width:100%;height:100%;overflow:hidden;background:var(--sky)}
  .card__bg{position:absolute;inset:0;width:100%;height:100%}

  .mascot{position:absolute;border-radius:40% 40% 30% 30%;
    background:linear-gradient(160deg,#9fd3f7 0%,#4caf50 35%,#3a8f3c 60%,#d33a2c 100%)}
  .card--front .mascot{left:92px;top:74px;width:205px;height:205px}
  .card--back .mascot{left:110px;top:14px;width:150px;height:170px}

  .brand{position:absolute;font-family:"Arimo",sans-serif;font-weight:700;color:var(--brand-orange);
    text-transform:uppercase;line-height:1.05;letter-spacing:.3px;white-space:nowrap}
  .brand span{display:block}
  .card--front .brand{left:30px;top:292px;font-size:21px}
  .card--back .brand{left:40px;top:192px;font-size:18px}

  .promo{position:absolute;left:4px;top:4px;display:flex;align-items:flex-start;gap:10px}
  .promo__amount{font-family:"Bitter",serif;font-weight:700;color:var(--accent-blue);font-size:52px;line-height:1}
  .promo__off{display:block;font-size:13px;margin-top:-8px;margin-left:18px}
  .promo__tagline{font-family:"Arimo",sans-serif;color:var(--accent-blue);font-size:13.5px;line-height:1.3;margin-top:10px}

  .offer{position:absolute;left:315px;top:76px;width:352px;color:var(--white);
    font-family:"Open Sans",sans-serif;font-size:16px;line-height:1.28;text-align:center}
  .offer p+p{margin-top:20px}

  .contact-bar{position:absolute;left:0;right:0;top:388px;display:flex;gap:80px;padding-left:108px;
    font-family:"Bitter",serif;font-weight:700;font-size:17px;color:var(--ink);align-items:center}
  .contact{display:flex;align-items:center;gap:8px}
  .icon{width:24px;height:24px;flex:none}

  .details{position:absolute;left:292px;top:52px;font-family:"Bitter",serif;color:var(--ink)}
  .details__phone{display:flex;align-items:center;gap:6px;font-style:italic;font-size:22px;font-weight:700}
  .details__web{display:flex;align-items:center;gap:6px;font-size:17px;font-weight:700;margin-top:2px}
  .details__lic{font-family:"Arimo",sans-serif;font-size:13px;margin:6px 0 0 36px}

  .slogan{position:absolute;inset:0;width:100%;height:100%}
  .slogan text{font-family:"Arimo",sans-serif;font-weight:700;font-size:18px;fill:var(--slogan)}

  .referral-form{position:absolute;left:123px;top:268px;font-family:"Bitter",serif;font-weight:700;font-size:19px;color:var(--ink)}
  .referral-form__row{display:flex;align-items:flex-end;height:46px}
  .referral-form__label{width:169px}
  .referral-form__line{width:295px;border-bottom:2px solid var(--ink);height:22px}
</style>
</head>
<body>
<main class="canvas">

  <section class="card card--front">
    <div class="card__face">
      <svg class="card__bg" viewBox="0 0 690 432" preserveAspectRatio="none" aria-hidden="true">
        <path d="M0 0H690V30C560 40 420 70 260 80C160 86 60 100 0 108Z" fill="var(--sun)"/>
        <path d="M0 372C180 360 330 320 480 290C580 270 650 250 690 235V432H0Z" fill="var(--orange)"/>
        <path d="M0 400C200 385 420 360 690 320V432H0Z" fill="var(--orange-light)" opacity=".6"/>
      </svg>

      <div class="promo">
        <div class="promo__amount">$25<span class="promo__off">OFF</span></div>
        <p class="promo__tagline">Tell a friend, if i was giving away cash vouchers.<br>keep me in your wallet and pass me on (dont use this)!</p>
      </div>

      <div class="mascot" role="img" aria-label="Cartoon electrician superhero holding a light bulb"></div>
      <p class="brand"><span>Bright Spark</span><span>Electrical Pty Ltd</span></p>

      <div class="offer">
        <p>If you’re happy with our service, we would really love for you to recommend us to your friends. If your friends use our service we will give you 2 FREE movie tickets &amp; your friends $25 OFF their service</p>
        <p>*this offer is only valued for work over $55. Non transferable for cash. This coupon is limited to 1 per customer, not to be used in conjunction with any other offer</p>
      </div>

      <div class="contact-bar">
        <span class="contact">
          <svg class="icon" viewBox="0 0 24 24" aria-hidden="true"><circle cx="12" cy="12" r="10" fill="var(--accent-blue)"/></svg>
          www.brightsparkelectrical.com.au
        </span>
        <span class="contact">
          <svg class="icon" viewBox="0 0 24 24" aria-hidden="true"><path d="M6 3l4 4-2 3c1 2 3 4 6 6l3-2 4 4-3 3C10 20 4 14 3 6z" fill="var(--accent-blue)"/></svg>
          1300 846 572
        </span>
      </div>
    </div>
  </section>

  <section class="card card--back">
    <div class="card__face">
      <svg class="card__bg" viewBox="0 0 694 430" preserveAspectRatio="none" aria-hidden="true">
        <path d="M0 262C200 255 420 232 694 148V430H0Z" fill="var(--orange)"/>
        <path d="M0 330C200 322 430 295 694 240V430H0Z" fill="var(--orange-light)" opacity=".55"/>
      </svg>

      <div class="mascot" role="img" aria-label="Cartoon electrician superhero holding a light bulb"></div>
      <p class="brand"><span>Bright Spark</span><span>Electrical Pty Ltd</span></p>

      <div class="details">
        <p class="details__phone">
          <svg class="icon" viewBox="0 0 24 24" aria-hidden="true"><path d="M6 3l4 4-2 3c1 2 3 4 6 6l3-2 4 4-3 3C10 20 4 14 3 6z" fill="var(--accent-blue)"/></svg>
          1300 846 572
        </p>
        <p class="details__web">
          <svg class="icon" viewBox="0 0 24 24" aria-hidden="true"><circle cx="12" cy="12" r="10" fill="var(--accent-blue)"/></svg>
          www.brightsparkelectrical.com.au
        </p>
        <p class="details__lic">Lic no: 418695D</p>
      </div>

      <svg class="slogan" viewBox="0 0 694 430" aria-hidden="true">
        <path id="slogan-curve" d="M252 226C390 222 540 200 676 146" fill="none"/>
        <text textLength="410" lengthAdjust="spacingAndGlyphs"><textPath href="#slogan-curve">Sydney's Foremost Residential Electricians</textPath></text>
      </svg>

      <div class="referral-form">
        <div class="referral-form__row"><span class="referral-form__label">Refferee name :</span><span class="referral-form__line"></span></div>
        <div class="referral-form__row"><span class="referral-form__label">Address&nbsp;&nbsp;&nbsp;&nbsp;&nbsp;&nbsp;&nbsp;&nbsp;&nbsp;&nbsp;:</span><span class="referral-form__line"></span></div>
        <div class="referral-form__row"><span class="referral-form__label">Friends Name :</span><span class="referral-form__line"></span></div>
      </div>
    </div>
  </section>

</main>
</body>
</html>
```